Book Flyer

I want a flyer that we can use to promote this book to educators and to leaders....below is a sample flyer but I want something bold and creative and different from this....it can be completely different from what is attached. I want to be a WOW to increase sales. Please include pic of book and how folks can get a copy....I've given you a few pics but please be creative ....looking for a wow.

```html
<!DOCTYPE html>
<html lang="en">
<head>
<meta charset="utf-8">
<title>Definitive Excellence – Book Flyer</title>
<link rel="stylesheet" href="https://fonts.googleapis.com/css2?family=Bebas+Neue&family=Poppins:ital,wght@0,300;0,400;0,600;0,700;1,400;1,600&display=swap">
<style>
  :root{
    --navy:#141d3d;
    --red:#e64142;
    --yellow:#fdd10b;
    --blue:#2a7cc7;
    --white:#ffffff;
    --ink:#1b1b1b;
    --stage:#6f7b83;
    --rule:#c9ccd3;
  }
  *{box-sizing:border-box;margin:0;padding:0}
  html,body{width:1200px;height:2400px;overflow:hidden}
  body{background:var(--stage);font-family:"Poppins",sans-serif;position:relative}
  .flyer{position:absolute;left:40px;top:408px;width:1120px;height:1584px;background:var(--white);overflow:hidden}
  .flyer > *{position:absolute}
  .backdrop{left:0;top:0;width:1120px;height:1584px}

  .title-block{left:68px;top:81px;width:500px;height:125px;background:var(--red);
    font-family:"Bebas Neue",sans-serif;color:var(--white);font-size:126px;line-height:132px;text-align:center;letter-spacing:1px}
  .title-sub{left:68px;top:220px;font-weight:300;color:var(--yellow);font-size:60px;line-height:64px;letter-spacing:1px}

  .endorsement{left:68px;top:345px;width:444px;color:var(--white);font-size:22.5px;line-height:27.2px;font-weight:400;text-align:justify}
  .endorsement .mark{color:var(--red);font-family:"Poppins",sans-serif;font-weight:700;font-size:52px;line-height:0;vertical-align:-14px;margin-right:10px}
  .endorsement .mark.close{margin:0 0 0 6px}
  .endorser{left:286px;top:676px;color:var(--white);font-size:23px;line-height:28px}
  .endorser .first{color:var(--yellow);font-style:italic;font-weight:600}
  .endorser .last{font-style:italic;font-weight:600}

  .book-shot{left:0;top:0;width:1120px;height:1584px;pointer-events:none}

  .strategies-head{left:384px;top:1028px;width:639px;height:51px;background:var(--navy);
    color:var(--white);font-weight:700;font-size:24.5px;line-height:51px;text-align:center}
  .strategies-head .accent{color:var(--yellow)}

  .strategy{top:1100px;height:170px;font-size:16px;line-height:18.5px;color:var(--ink)}
  .strategy + .strategy{border-left:1.5px solid var(--rule)}
  .equity{left:373px;width:205px;padding:0 14px 0 0}
  .change{left:578px;width:221px;padding:0 14px 0 17px}
  .communication{left:799px;width:221px;padding:0 10px 0 17px}
  .strategy h3{display:flex;align-items:center;gap:8px;font-size:18.5px;font-weight:600;margin-bottom:12px;line-height:32px}
  .strategy h3 .icon{width:32px;height:32px;display:block}
  .equity h3{color:var(--red)}
  .change h3{color:var(--yellow)}
  .communication h3{color:var(--blue)}
  .strategy p{text-align:justify}
  .strategy .q{font-weight:700;font-size:24px;line-height:0;vertical-align:-7px}
  .equity .q{color:var(--red)}
  .change .q{color:var(--yellow)}
  .communication .q{color:var(--blue)}
  .strategy cite{display:block;text-align:right;font-style:italic;font-weight:700;font-size:15.5px;margin-top:12px}

  .about{left:350px;top:1288px;width:770px;height:228px;background:var(--red);padding:22px 44px 0 40px;color:var(--white)}
  .about h2{font-size:28px;line-height:32px;font-weight:400;margin-bottom:6px}
  .about h2 .label{color:var(--yellow);font-weight:700}
  .about h2 .name{font-style:italic}
  .about p{font-size:13.6px;line-height:17px;text-align:justify}

  .portrait{left:34px;top:983px;width:328px;height:601px}

  .contact{right:50px;top:1532px;display:flex;align-items:center;gap:8px;color:var(--blue);font-weight:700;font-size:25px;line-height:34px}
</style>
</head>
<body>
<main class="flyer">

  <svg class="backdrop" viewBox="0 0 1120 1584" aria-hidden="true">
    <path fill="var(--red)" d="M0 0H1120V1050C1095 1050 1080 990 1065 930C1045 850 1000 820 960 860C920 900 880 800 760 830C600 880 520 945 330 945C200 945 100 915 0 905Z"/>
    <path fill="var(--blue)" d="M0 0H1120V880C1040 880 990 720 880 730C720 750 580 820 400 852C250 876 120 872 0 868Z"/>
    <path fill="var(--yellow)" d="M0 0H1120V560C980 562 820 640 680 722C520 812 330 852 0 852Z"/>
    <path fill="var(--navy)" d="M0 0H1120V538C960 546 800 620 660 700C500 790 300 834 0 838Z"/>
    <polygon fill="var(--yellow)" points="915,147 955,147 948,193"/>
    <polygon fill="var(--red)" points="853,186 933,265 865,272"/>
    <polygon fill="var(--yellow)" points="74,746 158,700 164,790"/>
    <polygon fill="var(--yellow)" points="898,972 940,1006 895,1006"/>
    <polygon fill="var(--yellow)" points="345,950 384,990 344,992"/>
    <polygon fill="var(--blue)" points="283,972 361,1038 282,1068"/>
    <polygon fill="var(--yellow)" points="34,1367 62,1336 62,1404"/>
    <polygon fill="var(--blue)" points="0,1425 34,1460 0,1470"/>
  </svg>

  <h1 class="title-block">DEFINITIVE</h1>
  <div class="title-sub">EXCELLENCE</div>

  <blockquote class="endorsement">
    <span class="mark">&ldquo;</span>Definitive Excellence is a book written for all leaders. Dr. Marcus Vale speaks from real life experiences that are relatable and from the heart. His leadership steps have helped him develop into one of the most accomplished administrative leaders in the country. The three specific strategies outlined in this will transform your leadership skills and help you stay track to ensure success.<span class="mark close">&rdquo;</span>
  </blockquote>
  <p class="endorser">-<span class="first">Karen</span> <span class="last">Whitfield</span>,<br>Principal</p>

  <svg class="book-shot" viewBox="0 0 1120 1584" role="img" aria-label="Hardcover book mockup of Definitive Excellence by R. Marcus Vale, foreword by Leon Hartley, with rising arrows on the cover">
    <defs>
      <linearGradient id="coverTone" x1="0" y1="0" x2="0.25" y2="1">
        <stop offset="0" stop-color="#1d2a55"/>
        <stop offset="0.42" stop-color="#2f5a9c"/>
        <stop offset="0.5" stop-color="#e64142"/>
        <stop offset="0.66" stop-color="#e64142"/>
        <stop offset="0.7" stop-color="#f4f4f4"/>
        <stop offset="1" stop-color="#e9e9ec"/>
      </linearGradient>
    </defs>
    <polygon fill="#d9dadf" points="1043,362 1062,372 852,1004 828,994"/>
    <polygon fill="url(#coverTone)" points="727,288 1043,362 828,994 501,859"/>
  </svg>

  <h2 class="strategies-head"><span class="accent">3 Fundamental Strategies</span> That Drive Leadership</h2>

  <section class="strategy equity">
    <h3><svg class="icon" viewBox="0 0 32 32"><rect width="32" height="32" rx="3" fill="var(--red)"/><g fill="#fff"><circle cx="9" cy="10" r="2.6"/><circle cx="16" cy="10" r="2.6"/><circle cx="23" cy="10" r="2.6"/><rect x="7" y="14" width="4" height="11"/><rect x="14" y="14" width="4" height="11"/><rect x="21" y="14" width="4" height="11"/></g></svg>EQUITY</h3>
    <p><span class="q">&ldquo;</span>Fariness does not mean everyone gets the same. Fairness means everyone gets what they need.<span class="q">&rdquo;</span></p>
    <cite>-Mara Ellison</cite>
  </section>

  <section class="strategy change">
    <h3><svg class="icon" viewBox="0 0 32 32"><rect width="32" height="32" rx="3" fill="var(--yellow)"/><g fill="none" stroke="#fff" stroke-width="2.6" stroke-linecap="round"><path d="M8 13h14l-4-4"/><path d="M24 19H10l4 4"/></g></svg>CHANGE</h3>
    <p><span class="q">&ldquo;</span>If you do not change direction, you may end up where you are heading.<span class="q">&rdquo;</span></p>
    <cite>-Lin Hao</cite>
  </section>

  <section class="strategy communication">
    <h3><svg class="icon" viewBox="0 0 32 32"><rect width="32" height="32" rx="3" fill="var(--blue)"/><g fill="#fff"><circle cx="11" cy="11" r="3"/><circle cx="21" cy="11" r="3"/><rect x="7" y="16" width="8" height="8" rx="2"/><rect x="17" y="16" width="8" height="8" rx="2"/></g></svg>COMMUNICATION</h3>
    <p><span class="q">&ldquo;</span>The single bigge problem in communica-tion is th illusion that is has taken place.<span class="q">&rdquo;</span></p>
    <cite>-Henry Colbert</cite>
  </section>

  <section class="about">
    <h2><span class="label">ABOUT</span> <span class="name">Dr. Vale</span></h2>
    <p>Distinguished as a vibrant, visionary, and innovative leader who recognizes that humility is the most important trait a leader can possess, Dr. Vale uses his prior experiences in business, education, and nonprofit to assist organization leaders from all industries build internal leadership capacity, including strategy &amp; talent management and development to maximize organizational potential and success.ciosqu ad litora torquent per conubia nostra, per inceptos himenaeos. Mauris in erat justo. Nullam ac urna eu felis dapibus condimentum sit amet a augue. Sed non neque elit. Sed ut imperdiet nisi. Proin condimentum fermentum nunc. Etiam pharetra, erat sed fermentum feugiat, velit mauris egestas quam, ut aliquam massa nisl quis neque. Suspendisse in orci enim.</p>
  </section>

  <div class="portrait" role="img" aria-label="Portrait of Dr. Marcus Vale standing with arms crossed, in a light blue shirt and patterned tie" style="background:linear-gradient(180deg,#ffffff 0%,#dfe6f1 30%,#c9d3e4 60%,#5a5d66 82%,#3d4048 100%)"></div>

  <p class="contact"><svg width="30" height="22" viewBox="0 0 30 22" aria-hidden="true"><rect x="1.5" y="1.5" width="27" height="19" fill="none" stroke="var(--red)" stroke-width="3"/><path d="M2 2l13 10L28 2" fill="none" stroke="var(--red)" stroke-width="3"/></svg>info@thevalegroup.com</p>

</main>
</body>
</html>
```